Launch Website

A very simple, but attractive website (template preferred) is required in a common format - HTML5 or Wordpress etc.
It should be easily user updateable for updates.
Pages it needs:
-Home Page with menu bar, company logo and 1 large graphic/picture and two smaller graphics/logos.
- What we do
- How we do it
- About Us
- Guarantees
- Results
- Contact Page with Enquiry Form
- Provision for a blog to be added later

Most pages will be approx 150 words text with some small/medium images.
We have our own domain & hosting.

A "less is more" design approach would be encouraged.

Target Market(s)

Vehicle Fleet Managers

Industry/Entity Type

It Company

Font styles to use
Sans Serif

Colors
9bcb3c

Requirements
Must have
• Corporate Style. No Fluff.
Nice to have
• Images of LIght Commerical vehicles and trucks

Am ok with white background throughout site.
Colours should match/complement company logo.
Should not have
• Should not be too "busy"

```html
<!DOCTYPE html>
<html lang="en">
<head>
<meta charset="utf-8">
<title>Arcline Motive – Diesel Fleet Engine Optimisation</title>
<link rel="stylesheet" href="https://fonts.googleapis.com/css2?family=Open+Sans:wght@400;600&family=Titillium+Web:wght@300;400&family=Tinos&display=swap">
<style>
  :root {
    --ink: #2e2e2e;
    --muted: #666666;
    --faint: #8a8a8a;
    --rule: #dcdcdc;
    --brand-blue: #00a6f0;
    --dark-btn: #2b2b2b;
    --card-bg: #f7f6f4;
    --band-yellow: #f0e035;
    --bg-a: #fbfbfb;
    --bg-b: #f3f3f3;
    --grey-btn: #6e6e6e;
    --white: #ffffff;
  }
  * { box-sizing: border-box; margin: 0; padding: 0; }
  html, body { width: 1200px; height: 1178px; overflow: hidden; }
  body {
    font-family: "Open Sans", Arial, sans-serif;
    color: var(--ink);
    background: repeating-linear-gradient(135deg, var(--bg-a) 0 3px, var(--bg-b) 3px 5px);
  }
  .page { position: relative; width: 1200px; height: 1178px; }

  .brand { position: absolute; left: 26px; top: 36px; display: flex; align-items: center; gap: 12px; }
  .brand-dot { width: 34px; height: 34px; border-radius: 50%; background: var(--brand-blue); }
  .brand-name { font-size: 36px; font-weight: 600; color: var(--brand-blue); letter-spacing: -0.5px; }
  .phone { position: absolute; right: 24px; top: 50px; font-size: 16.5px; color: var(--ink); }

  .main-nav {
    position: absolute; left: 24px; top: 133px; width: 1152px; height: 62px;
    border-top: 1px solid var(--rule); border-bottom: 1px solid var(--rule);
    background: var(--white);
    display: flex; justify-content: space-between; align-items: center; padding: 0 22px;
  }
  .main-nav a { font-size: 16.8px; color: var(--ink); text-decoration: none; text-transform: uppercase; }

  .hero { position: absolute; left: 36px; top: 212px; width: 1128px; height: 577px; overflow: hidden; }
  .hero-photo {
    position: absolute; inset: 0;
    background: linear-gradient(180deg, #8fb4da 0%, #c9dbee 30%, #eef2f6 52%, #c9c9c6 78%, #8c8a86 100%);
  }
  .hero-truck {
    position: absolute; left: 580px; top: 10px; width: 520px; height: 560px;
    background: linear-gradient(180deg, #e9e4c8 0%, #e6cf2c 25%, #d9bf1f 60%, #3a3a38 100%);
    border-radius: 10px; opacity: 0.85;
  }
  .hero-band { position: absolute; left: 0; top: 238px; width: 1128px; height: 100px; background: var(--band-yellow); }
  .hero-copy { position: absolute; left: 104px; top: 196px; font-family: "Titillium Web", Arial, sans-serif; color: #1e1e1e; }
  .hero-lead { font-size: 30px; font-weight: 400; line-height: 38px; }
  .hero-save { font-size: 44px; font-weight: 300; line-height: 42px; margin-top: 10px; }
  .hero-figure { font-size: 62px; font-weight: 300; line-height: 56px; }
  .hero-tail { font-size: 30px; font-weight: 400; line-height: 40px; margin-top: 12px; }
  .hero-arrow { position: absolute; top: 258px; }
  .hero-arrow.prev { left: 34px; }
  .hero-arrow.next { right: 30px; }
  .partner-badge { position: absolute; top: 470px; width: 156px; height: 71px; background: var(--white); }
  .partner-badge.one { left: 112px; }
  .partner-badge.two { left: 270px; }

  .feature { position: absolute; top: 809px; width: 360px; height: 194px; background: var(--card-bg); text-align: center; padding-top: 24px; }
  .feature.about { left: 36px; border: 6px solid var(--brand-blue); padding-top: 18px; background: var(--card-bg); }
  .feature.what { left: 420px; }
  .feature.how { left: 804px; }
  .feature h2 { font-size: 21.5px; font-weight: 400; letter-spacing: 0.3px; color: #222; }
  .feature p { font-size: 16.6px; line-height: 24px; color: var(--muted); margin: 14px 28px 0; }
  .read-more {
    position: absolute; left: 50%; transform: translateX(-50%); bottom: 24px;
    width: 89px; height: 29px; line-height: 29px; font-family: "Tinos", "Times New Roman", serif;
    font-size: 14px; color: var(--white); background: var(--dark-btn); text-decoration: none;
  }
  .feature.about .read-more { background: var(--brand-blue); bottom: 18px; }

  .rule { position: absolute; left: 24px; width: 1152px; height: 1px; background: var(--rule); }
  .rule.top { top: 1023px; }
  .rule.bottom { top: 1118px; }

  .connect-title { position: absolute; left: 42px; top: 1057px; font-size: 22px; color: #444; }
  .social { position: absolute; top: 1043px; width: 54px; height: 54px; border-radius: 50%; background: #ececec; display: flex; align-items: center; justify-content: center; }
  .social.one { left: 338px; }
  .social.two { left: 397px; background: var(--brand-blue); }
  .social.three { left: 458px; }
  .divider-v { position: absolute; left: 600px; top: 1042px; width: 1px; height: 58px; background: var(--rule); }
  .newsletter-title { position: absolute; left: 629px; top: 1052px; font-size: 21px; line-height: 19px; color: #444; }
  .newsletter-form { position: absolute; left: 804px; top: 1049px; display: flex; }
  .newsletter-form .email {
    width: 260px; height: 41px; border: 1px solid #dadada; background: var(--white);
    font-size: 12px; color: var(--faint); padding: 0 13px; line-height: 39px;
  }
  .newsletter-form .subscribe {
    width: 100px; height: 41px; background: var(--grey-btn); color: var(--white);
    font-family: "Tinos", "Times New Roman", serif; font-size: 16px; text-align: center; line-height: 41px;
  }
  .copyright { position: absolute; left: 38px; top: 1142px; font-size: 14px; color: var(--faint); }
</style>
</head>
<body>
<div class="page">
  <header>
    <div class="brand"><span class="brand-dot"></span><span class="brand-name">Arcline Motive</span></div>
    <div class="phone">Call us +1 800 555 0199</div>
    <nav class="main-nav">
      <a href="#">Home</a><a href="#">What we do</a><a href="#">How we do it</a><a href="#">About us</a>
      <a href="#">Guarantees</a><a href="#">Results</a><a href="#">Testimonials</a><a href="#">Contact us</a><a href="#">Blog</a>
    </nav>
  </header>

  <section class="hero">
    <div class="hero-photo" role="img" aria-label="Photo of a yellow semi truck driving on an open road under a cloudy sky"></div>
    <div class="hero-band"></div>
    <div class="hero-truck" role="img" aria-label="Yellow semi truck in front of the slide band"></div>
    <div class="hero-copy">
      <p class="hero-lead">We help diesel vehicle fleets</p>
      <p class="hero-save">SAVE UP TO</p>
      <p class="hero-figure">20% FUEL COSTS</p>
      <p class="hero-tail">by optimising their engines.</p>
    </div>
    <svg class="hero-arrow prev" width="34" height="66" viewBox="0 0 34 66" aria-hidden="true"><polyline points="32,2 2,33 32,64" fill="none" stroke="#555" stroke-width="1.5"/></svg>
    <svg class="hero-arrow next" width="34" height="66" viewBox="0 0 34 66" aria-hidden="true"><polyline points="2,2 32,33 2,64" fill="none" stroke="#555" stroke-width="1.5"/></svg>
    <div class="partner-badge one" role="img" aria-label="Industry association membership badge"></div>
    <div class="partner-badge two" role="img" aria-label="Partner badge"></div>
  </section>

  <section class="feature about">
    <h2>ABOUT ARCLINE MOTIVE</h2>
    <p>Fleetcore have combined over 50 years experience in all aspects of…</p>
    <a class="read-more" href="#">Read more</a>
  </section>
  <section class="feature what">
    <h2>WHAT WE DO</h2>
    <p>Fleetcore delivers award winning, ISO 9001 certified diesel engine…</p>
    <a class="read-more" href="#">Read more</a>
  </section>
  <section class="feature how">
    <h2>HOW WE DO IT</h2>
    <p>Fleetcore will conduct an obligation Free Consultation with your Fleet…</p>
    <a class="read-more" href="#">Read more</a>
  </section>

  <footer>
    <div class="rule top"></div>
    <div class="connect-title">CONNECT WITH US</div>
    <span class="social one" aria-label="Social profile"></span>
    <span class="social two" aria-label="Social profile"></span>
    <span class="social three" aria-label="Email us">
      <svg width="20" height="14" viewBox="0 0 20 14" aria-hidden="true"><rect x="1" y="1" width="18" height="12" fill="none" stroke="#555" stroke-width="1.6"/><polyline points="1,1 10,8 19,1" fill="none" stroke="#555" stroke-width="1.6"/></svg>
    </span>
    <div class="divider-v"></div>
    <div class="newsletter-title">NEWSLETTER<br>SIGN UP</div>
    <div class="newsletter-form">
      <div class="email">Your email</div>
      <div class="subscribe">subscribe</div>
    </div>
    <div class="rule bottom"></div>
    <div class="copyright">© 2014 Arcline Motive. All rights reserved.</div>
  </footer>
</div>
</body>
</html>
```